Menubook for a 2star restaurant

Hey,
We are looking for a new menu for a 2 star restaurant in Belgium. They want a clean, abstract, with small light accents of gold, copper. The format will be 21 cm by 21 cm. and the booklet will have 4 printable sides inc front & back. Only the logo on the front. The wine list will be separate so it should not be included in the design. "Bites" - "voorgerechten" - "hoofdgerechten" & "nagerechten" must be copied.

Industry/Entity Type

Restaurant

Requirements
Must have
• Clean look
Nice to have
• touches of gold

```html
<!DOCTYPE html>
<html lang="nl">
<head>
<meta charset="utf-8">
<title>Fiamma by Lore — Menukaart</title>
<link rel="stylesheet" href="https://fonts.googleapis.com/css2?family=Didact+Gothic&family=Montserrat:wght@600&display=swap">
<style>
  :root {
    --backdrop: #9a8a5c;
    --paper: #f6f6f6;
    --paper-grey-a: #e6e6e6;
    --paper-grey-b: #cfcfcf;
    --ink: #3c3c3c;
    --ink-soft: #5a5a5a;
    --gold: #c9a46a;
    --gold-pale: rgba(201, 164, 106, 0.22);
  }
  * { box-sizing: border-box; margin: 0; padding: 0; }
  html, body { width: 1200px; height: 1118px; overflow: hidden; }
  body {
    background: var(--backdrop);
    font-family: "Didact Gothic", sans-serif;
    color: var(--ink);
    position: relative;
  }
  .spread {
    position: absolute;
    left: 80px;
    width: 1040px;
    height: 520px;
    display: flex;
  }
  .spread--inside { top: 24px; }
  .spread--outside { top: 574px; }
  .page {
    position: relative;
    width: 520px;
    height: 520px;
    overflow: hidden;
  }
  .page--white { background: var(--paper); }
  .page--grey { background: linear-gradient(135deg, var(--paper-grey-a), var(--paper-grey-b)); }

  .frame { position: absolute; left: 0; top: 0; width: 520px; height: 520px; }
  .frame rect { fill: none; stroke: var(--gold); stroke-width: 1; }

  .ornament { position: absolute; }
  .ornament--sun-corner { background: radial-gradient(circle at var(--ox) var(--oy), var(--gold-pale), transparent 70%); }
  .ornament--spark { background: radial-gradient(circle, var(--gold-pale), transparent 70%); }

  .menu-block { position: absolute; }
  .menu-block h2 {
    font-family: "Montserrat", sans-serif;
    font-weight: 600;
    font-size: 9.5px;
    letter-spacing: 0.3px;
    color: var(--ink);
    margin-bottom: 20px;
  }
  .menu-group { margin-bottom: 16px; }
  .menu-item {
    display: flex;
    justify-content: space-between;
    align-items: flex-start;
    font-size: 8.5px;
    line-height: 1.15;
    text-transform: uppercase;
    color: var(--ink);
    margin-bottom: 6px;
  }
  .menu-item .price { text-transform: none; text-align: right; }
  .menu-item small { text-transform: none; font-size: 6px; }
  .menu-item .desc {
    display: block;
    text-transform: none;
    font-size: 6.5px;
    color: var(--ink-soft);
    margin-top: 3px;
    padding-left: 4px;
    line-height: 1.45;
  }
  .dish { margin-bottom: 20px; }
  .section-gap { margin-top: 36px; }

  .brand {
    position: absolute;
    left: 150px;
    top: 250px;
    width: 260px;
    text-align: center;
    font-size: 24px;
    letter-spacing: 10px;
    color: var(--ink);
    text-transform: lowercase;
  }
</style>
</head>
<body>

<section class="spread spread--inside">
  <article class="page page--grey">
    <div class="ornament ornament--spark" style="left:40px;top:40px;width:60px;height:60px" role="img" aria-label="Kleine gouden sterretjes"></div>
    <div class="ornament ornament--sun-corner" style="--ox:0%;--oy:100%;left:0;top:410px;width:110px;height:110px" role="img" aria-label="Gouden zonnestralen in de hoek"></div>
    <svg class="frame" viewBox="0 0 520 520" aria-hidden="true">
      <rect x="88" y="95" width="382" height="390"/>
      <rect x="92" y="99" width="374" height="382"/>
    </svg>
    <div class="menu-block" style="left:178px;top:168px;width:215px">
      <h2>APERITIVI</h2>
      <div class="menu-group">
        <div class="menu-item"><span>Casa del Colle</span><span class="price">19</span></div>
        <div class="menu-item"><span>Charles Montreuil</span><span class="price">21</span></div>
      </div>
      <div class="menu-group">
        <div class="menu-item"><span>Arancio Spritz</span><span class="price">15</span></div>
        <div class="menu-item"><span>Hugo</span><span class="price">15</span></div>
      </div>
      <div class="menu-group">
        <div class="menu-item"><span>Gin Marea</span><span class="price">18</span></div>
        <div class="menu-item"><span>Copperleaf</span><span class="price">19</span></div>
        <div class="menu-item"><span>Nova Gin <span style="text-transform:none">(non alcoholisch)</span></span><span class="price">19</span></div>
      </div>
      <div class="menu-group">
        <div class="menu-item"><span>Negroni Sbagliato</span><span class="price">17</span></div>
        <div class="menu-item"><span>Classic Negroni</span><span class="price">19</span></div>
        <div class="menu-item"><span>Amaretto Sunrise</span><span class="price">15</span></div>
      </div>
    </div>
  </article>

  <article class="page page--white">
    <div class="ornament ornament--sun-corner" style="--ox:100%;--oy:0%;left:400px;top:0;width:120px;height:120px" role="img" aria-label="Gouden zonnestralen in de hoek"></div>
    <div class="ornament ornament--spark" style="left:455px;top:150px;width:50px;height:50px" role="img" aria-label="Kleine gouden sterretjes"></div>
    <div class="ornament ornament--spark" style="left:20px;top:440px;width:55px;height:55px" role="img" aria-label="Kleine gouden sterretjes"></div>
    <svg class="frame" viewBox="0 0 520 520" aria-hidden="true">
      <rect x="82" y="95" width="382" height="390"/>
      <rect x="86" y="99" width="374" height="382"/>
    </svg>
    <div class="menu-block" style="left:157px;top:150px;width:235px">
      <h2>BITES</h2>
      <div class="menu-item"><span>Oester Belmare <small>(1st)</small><span class="desc">jalapeño | komkommer | ajo blanco<br>supplement kaviaar 5gr (+ €18)</span></span><span class="price">9</span></div>
      <div class="menu-item" style="margin-top:8px"><span><span style="text-transform:none">'nduja</span> Risotto Croquettes <small>(2st)</small></span><span class="price">9</span></div>
      <div class="menu-item" style="margin-top:8px"><span>Charcuterie<span class="desc">cornichon | olijven</span></span><span class="price">15</span></div>
      <div class="menu-item" style="margin-top:8px"><span>Koude Amandel-Knoflook Zuppa<span class="desc">fregola | kreeft</span></span><span class="price">14</span></div>
      <h2 class="section-gap">VOORGERECHTEN</h2>
      <div class="menu-item"><span>Antipasti &nbsp;*</span><span class="price">35 p.p.</span></div>
      <div class="menu-item" style="margin-top:20px"><span>Pizzetta Amaro<span class="desc">met 1/2 kreeft | doperwt | basilicum | courgette<br>ook vegetarisch te bestellen</span></span><span class="price"><br>37<br>32</span></div>
    </div>
  </article>
</section>

<section class="spread spread--outside">
  <article class="page page--white">
    <div class="ornament ornament--sun-corner" style="--ox:100%;--oy:0%;left:380px;top:0;width:140px;height:130px" role="img" aria-label="Gouden zonnestralen rond de vouw"></div>
    <div class="ornament ornament--sun-corner" style="--ox:0%;--oy:100%;left:0;top:400px;width:120px;height:120px" role="img" aria-label="Gouden zonnestralen in de hoek"></div>
    <div class="menu-block" style="left:155px;top:58px;width:240px">
      <h2>HOOFDGERECHTEN</h2>
      <div class="menu-item dish"><span>Spaghetti Vongole *<span class="desc">bosui | piemento | zilte groenten</span></span><span class="price">29</span></div>
      <div class="menu-item dish"><span>Kabeljauw Rug *<span class="desc">limoen | kappertjes | mosselen | safraan</span></span><span class="price">36</span></div>
      <div class="menu-item dish"><span>Kalfsfilet *<span class="desc">paarse bloemkool | girolle | groen asperge | daslook | pijpajuin</span></span><span class="price">46</span></div>
      <div class="menu-item dish"><span>Insalate del Giorno<span class="desc">vlees of vis<br>veggie</span></span><span class="price"><br>40<br>33</span></div>
      <div class="menu-item dish"><span>Gnocchi<span class="desc">salie | spinazie | barilotto</span></span><span class="price">29</span></div>
      <div class="menu-item dish"><span>Gepocheerd Hoeve Ei<span class="desc">girolle | daslook | groene asperges</span></span><span class="price">36</span></div>
      <h2 class="section-gap" style="margin-top:30px">NAGERECHTEN</h2>
      <div class="menu-item" style="margin-bottom:12px"><span>Assortiment van 5 Italiaanse kazen</span><span class="price">27</span></div>
      <div class="menu-item"><span>Amalfi Citroen met Meringue *</span><span class="price">16</span></div>
      <div class="menu-item" style="margin-top:44px"><span>* Menu &nbsp;| &nbsp;5 Gangen</span><span class="price">95</span></div>
    </div>
  </article>

  <article class="page page--grey">
    <div class="ornament ornament--sun-corner" style="--ox:0%;--oy:0%;left:0;top:0;width:140px;height:130px" role="img" aria-label="Gouden zonnestralen rond de vouw"></div>
    <div class="ornament ornament--sun-corner" style="--ox:100%;--oy:100%;left:400px;top:400px;width:120px;height:120px" role="img" aria-label="Gouden zonnestralen in de hoek"></div>
    <div class="brand">fiamma by lore</div>
  </article>
</section>

</body>
</html>
```